Computer consultant business card

Plimvo Software is a newly started computer consulting company. It's a small one-man company that provides mostly Android applications but also websites in collaboration with designers. I'm running this company on the side of full time university studies.

I want the final design to be clean and memorable. Be creative! :)

Some inspiration:
http://www.artfenwick.com/design/62242
http://www.artfenwick.com/design/1628455/business-card-design-by-brusqlin
http://www.artfenwick.com/design/918507/business-card-design-by-velinora-quathbridge

See attachment for my company logo.
Updates

I would like to thank everyone for submitting! I'll need a couple of days to review and ultimately select a design.

Target Market(s)

Non-technical entrepreneurs and small companies.

Industry/Entity Type

University

Requirements
Must have
• My company logo.
In any way, both colors from my logo.
First- and last name, e-mail and phone number.
Double-sided design.
Nice to have
• Something creative with the symbol in my logo

```html
<!DOCTYPE html>
<html lang="en">
<head>
<meta charset="utf-8">
<title>Plimvo Software — Business Card</title>
<link rel="stylesheet" href="https://fonts.googleapis.com/css2?family=Open+Sans:wght@400;600;700&display=swap">
<style>
  :root {
    --page-bg: #e9e6e1;
    --card-black: #050505;
    --card-white: #ffffff;
    --brand-blue: #4a74bd;
    --brand-dark: #2b2b2b;
    --text-light: #f2f2f2;
  }
  * { box-sizing: border-box; margin: 0; padding: 0; }
  html, body {
    width: 1200px; height: 900px; overflow: hidden;
    background: var(--page-bg);
    font-family: "Open Sans", Arial, sans-serif;
  }
  .sheet {
    width: 1200px; height: 900px;
    display: flex; align-items: center; justify-content: center; gap: 44px;
  }
  .card {
    position: relative;
    width: 530px; height: 304px;
    border-radius: 24px;
    overflow: hidden;
    background: var(--card-black);
    box-shadow: 0 10px 24px rgba(0,0,0,.18);
  }

  /* Front */
  .card-front .halftone-band {
    position: absolute; inset: 0;
    background: linear-gradient(200deg,
      transparent 18%, rgba(90,90,90,.35) 36%, rgba(140,140,140,.55) 50%,
      rgba(90,90,90,.35) 64%, transparent 82%);
  }
  .wordmark {
    display: flex; align-items: center; gap: 14px;
    font-weight: 600; letter-spacing: .5px; line-height: 1;
  }
  .wordmark .mark-dot {
    border-radius: 50%; background: var(--brand-blue); flex: none;
  }
  .card-front .wordmark {
    position: absolute; left: 50%; top: 50%;
    transform: translate(-50%, -50%);
    color: var(--card-white); font-size: 70px;
  }
  .card-front .mark-dot { width: 44px; height: 44px; }

  /* Back */
  .card-back .white-panel { position: absolute; inset: 0; }
  .card-back .wordmark {
    position: absolute; left: 30px; bottom: 44px;
    color: var(--brand-dark); font-size: 42px; gap: 12px;
  }
  .card-back .mark-dot { width: 28px; height: 28px; }
  .identity {
    position: absolute; right: 30px; top: 34px; text-align: right;
  }
  .identity .person-name {
    color: var(--brand-blue); font-size: 25px; font-weight: 400; letter-spacing: .5px;
  }
  .identity .job-title {
    color: var(--text-light); font-size: 16px; font-weight: 700; margin-top: 2px;
  }
  .contact {
    position: absolute; right: 30px; bottom: 90px;
    list-style: none; text-align: right; color: var(--text-light);
    font-size: 14px; line-height: 1.9;
  }
  .contact li { display: flex; align-items: center; justify-content: flex-end; gap: 10px; }
  .contact svg { width: 13px; height: 13px; flex: none; }
</style>
</head>
<body>
<main class="sheet">

  <section class="card card-front" aria-label="Card front">
    <div class="halftone-band" role="img" aria-label="Diagonal grey halftone dot band"></div>
    <div class="wordmark"><span class="mark-dot"></span><span>Plimvo</span></div>
  </section>

  <section class="card card-back" aria-label="Card back">
    <svg class="white-panel" viewBox="0 0 530 304" preserveAspectRatio="none" aria-hidden="true">
      <path d="M0 304 L0 140 Q120 76 200 78 Q300 110 315 304 Z" fill="var(--brand-blue)"/>
      <path d="M0 304 L0 148 Q120 86 196 88 Q290 118 304 304 Z" fill="var(--card-black)"/>
      <path d="M0 304 L0 154 Q120 93 192 95 Q282 124 296 304 Z" fill="var(--card-white)"/>
    </svg>
    <div class="identity">
      <p class="person-name">YOUR NAME</p>
      <p class="job-title">Job Title</p>
    </div>
    <ul class="contact">
      <li>000-000-000
        <svg viewBox="0 0 14 14" aria-hidden="true"><rect x="3.5" y="1" width="7" height="12" rx="1.5" fill="none" stroke="currentColor" stroke-width="1.4"/></svg>
      </li>
      <li>name@domainname.com
        <svg viewBox="0 0 14 14" aria-hidden="true"><rect x="1" y="3" width="12" height="8" fill="currentColor"/><path d="M1 3 L7 8 L13 3" fill="none" stroke="var(--card-black)" stroke-width="1.2"/></svg>
      </li>
    </ul>
    <div class="wordmark"><span class="mark-dot"></span><span>Plimvo</span></div>
  </section>

</main>
</body>
</html>
```